Fresh Nest Builder Guide needs a new Landing Page

I like to get a landing page or website with 2-3 pages to help target home buyers who are looking to buy homes from builders such as PV Dwellings, Moritz, G.T. Falwick, etc. The landing page/website to be non-cluttered and be able to explain to home buyers that there are many benefits to include me as their buyer's agent when they buy a brand new home from any builders.
I may want to incorporate a short explanation video (animated) on the landing page and then for the viewer to click on a button that will take them to another page where they can search for new homes from different builders.
Target Market(s)
Home buyers looking to buy brand new home from builders such as PV Dwellings, Moritz, G.T. Falwick, etc.
Industry/Entity Type
Real Estate
Number of Pages Required
2 page
Requirements
Must have
- The landing page may have the explanation video at the bottom of the landing page (scrolled down) or there may be a CALL TO ACTION button that takes the viewer to the 2nd page to watch the explanation video. Once they watched the explanation video and are still interested, they can click on another CALL TO ACTION button that will take them to another website that they will be able to search for all the available new homes and register their contact information.
Should not have
- No clutters and no dark colors.

```html
<!DOCTYPE html>
<html lang="en">
<head>
<meta charset="utf-8">
<title>Fresh Nest Builder Guide</title>
<link href="https://fonts.googleapis.com/css2?family=Arvo:wght@400;700&family=Montserrat:wght@600;700&family=Open+Sans:wght@400;600;700&display=swap" rel="stylesheet">
<style>
:root{
  --yellow:#fdc51a;
  --yellow-deep:#f7b500;
  --purple:#a98ad6;
  --purple-deep:#8c6bc4;
  --ink:#1e1e1e;
  --text:#333;
  --muted:#9a9a9a;
  --line:#e4e4e4;
  --white:#fff;
  --red:#d9302a;
}
*{margin:0;padding:0;box-sizing:border-box}
html,body{width:1200px;height:3885px;overflow:hidden}
body{position:relative;background:var(--white);font-family:"Open Sans",sans-serif;color:var(--text)}
h1,h2,h3{font-weight:400}
.abs{position:absolute}
.slab{font-family:"Arvo",serif;font-weight:400;color:var(--ink)}

/* header */
.brand{left:130px;top:70px;display:flex;align-items:center;gap:14px}
.brand-dot{width:30px;height:30px;border-radius:50%;background:var(--yellow)}
.brand-name{font-family:"Arvo",serif;font-size:26px;color:#4a3b2e;line-height:1.1}
.nav{top:36px;left:915px;display:flex;gap:40px;align-items:center;font-size:11px;letter-spacing:2px;font-weight:600;color:#555}
.nav svg{margin-left:14px}

/* hero */
.hero-title{left:153px;top:292px;font-size:36px;line-height:48px;width:330px}
.hero-text{left:153px;top:408px;width:300px;font-size:12.5px;line-height:20px;color:var(--muted)}
.btn{display:flex;align-items:center;justify-content:center;gap:10px;background:var(--yellow);color:var(--white);border-radius:30px;font-size:12px;font-weight:700;letter-spacing:2px}
.hero-btn{left:153px;top:500px;width:160px;height:47px}
.laptop{left:518px;top:290px;width:524px;height:380px}
.laptop-shadow{left:560px;top:650px;width:440px;height:90px;border-radius:50%;background:radial-gradient(ellipse at center,rgba(0,0,0,.18),rgba(0,0,0,0) 70%)}

/* about band */
.about-band{left:0;top:764px;width:1200px;height:384px;background:var(--yellow)}
.candy{left:0;top:0;width:453px;height:384px;background:radial-gradient(circle at 220px 160px,#ffe07a 0,#ffc933 35%,var(--yellow) 62%)}
.tag{left:536px;top:92px;background:var(--purple-deep);color:var(--white);font-size:9px;font-weight:700;letter-spacing:1.5px;padding:3px 8px;border-radius:3px}
.about-title{left:536px;top:125px;font-family:"Arvo",serif;font-weight:400;font-size:34px;line-height:42px;color:var(--white)}
.about-sub{left:536px;top:234px;font-size:11.5px;color:var(--white)}
.round-arrow{left:1008px;top:169px}

/* values */
.eyebrow{left:228px;top:1296px;font-size:10px;letter-spacing:2px;color:#555}
.values-title{left:228px;top:1318px;font-size:36px}
.values-text{left:228px;top:1392px;width:360px;font-size:12.5px;line-height:22px;color:var(--muted)}
.values-list{left:228px;top:1458px;width:360px;font-size:12.5px;line-height:22px;color:var(--muted);list-style:none}
.values-list li::before{content:"• "}
.value{left:665px;width:380px}
.value-icon{position:absolute;left:0;top:0;width:58px;height:58px;border-radius:50%;background:var(--yellow);display:flex;align-items:center;justify-content:center}
.value-title{position:absolute;left:99px;top:0;font-family:"Arvo",serif;font-weight:400;font-size:19px;color:var(--ink)}
.value-text{position:absolute;left:99px;top:36px;width:275px;font-size:12.5px;line-height:24px;color:var(--muted)}
.divider{left:668px;top:1510px;width:368px;height:1px;background:var(--line)}

/* video band */
.video-band{left:0;top:1753px;width:1200px;height:677px;background:linear-gradient(135deg,#b39ae0,var(--purple) 50%,#9a7bd0)}
.video{left:155px;top:1842px;width:912px;height:510px;background:linear-gradient(180deg,#6d7f95 0%,#9aa3ab 35%,#d8d3cb 60%,#54604a 100%);box-shadow:0 20px 50px rgba(60,30,110,.35)}
.play{left:571px;top:2057px}

/* cta */
.cta-title{left:0;top:2524px;width:1200px;text-align:center;font-size:33px}
.cta-text{left:0;top:2578px;width:1200px;text-align:center;font-size:12.5px;line-height:21px;color:var(--muted)}
.cta-btn{left:508px;top:2639px;width:209px;height:42px}
.cta-faq{left:0;top:2696px;width:1200px;text-align:center;font-size:12px;color:var(--muted)}
.cta-faq a{color:var(--ink);text-decoration:underline}

/* builders */
.builders{left:0;top:2813px;width:1200px;height:378px;background:var(--yellow);display:flex;align-items:center;justify-content:space-around;padding:0 40px}
.builder{font-family:"Arvo",serif;font-weight:700;font-size:50px;color:var(--ink)}

/* contact */
.contact-title{left:130px;top:3325px;font-family:"Montserrat",sans-serif;font-weight:700;font-size:72px;line-height:93px;color:var(--ink);letter-spacing:1px}
.contact-line{left:130px;font-size:12.5px;color:var(--muted);display:flex;align-items:center;gap:18px}
.field{left:660px;width:389px;height:40px;border-bottom:1px solid var(--line)}
.field label{position:absolute;left:0;top:14px;font-size:9px;letter-spacing:1.5px;color:#666;font-weight:600}
.field span{position:absolute;left:82px;top:10px;font-size:14px;color:var(--ink)}
.field svg{position:absolute;right:4px;top:12px}
.req-star{position:absolute;right:6px;top:10px;color:var(--red);font-size:14px;font-style:normal}
.required{left:660px;top:3696px;font-size:11px;color:var(--muted)}
.required b{color:var(--red);margin-right:8px}
.submit{left:860px;top:3680px;width:186px;height:44px}
</style>
</head>
<body>

<header>
  <div class="abs brand"><span class="brand-dot"></span><span class="brand-name">Fresh Nest<br>Builder Guide</span></div>
  <nav class="abs nav"><span>ABOUT</span><span>CONTACT</span>
    <svg width="16" height="16" viewBox="0 0 16 16"><circle cx="6.5" cy="6.5" r="5" fill="none" stroke="#222" stroke-width="2"/><line x1="10" y1="10" x2="15" y2="15" stroke="#222" stroke-width="2"/></svg>
  </nav>
</header>

<section class="hero">
  <h1 class="abs slab hero-title">Not your average, agent</h1>
  <p class="abs hero-text">With a unique approach to what we do, we have established ourselves as the destination agency with proven results in the new home market.</p>
  <a class="abs btn hero-btn">START HERE</a>
  <div class="abs laptop-shadow"></div>
  <svg class="abs laptop" viewBox="0 0 524 380">
    <defs><linearGradient id="scr" x1="0" y1="0" x2="0" y2="1"><stop offset="0" stop-color="#6c7e95"/><stop offset=".45" stop-color="#c9c6c0"/><stop offset="1" stop-color="#4f5b46"/></linearGradient></defs>
    <rect x="38" y="0" width="448" height="340" rx="16" fill="#1c1c1e"/>
    <rect x="56" y="20" width="412" height="298" fill="url(#scr)" role="img" aria-label="Video still of a two-storey new home at dusk"/>
    <circle cx="262" cy="163" r="20" fill="none" stroke="#fff" stroke-width="2.5"/>
    <path d="M256 153 L272 163 L256 173 Z" fill="#fff"/>
    <path d="M0 342 H524 L510 362 Q505 368 495 368 H29 Q19 368 14 362 Z" fill="#c9cbce"/>
    <rect x="222" y="342" width="80" height="7" rx="3" fill="#a8abaf"/>
  </svg>
</section>

<section class="abs about-band">
  <div class="abs candy" role="img" aria-label="Swirled yellow lollipop with colourful sweets"></div>
  <span class="abs tag">ABOUT</span>
  <h2 class="abs about-title">Discover your dream home<br>Today</h2>
  <p class="abs about-sub">Find your place, your community.</p>
  <svg class="abs round-arrow" width="48" height="48" viewBox="0 0 48 48"><circle cx="24" cy="24" r="22" fill="none" stroke="#fff" stroke-width="2"/><path d="M14 24 H33 M26 17 L33 24 L26 31" fill="none" stroke="#fff" stroke-width="2"/></svg>
</section>

<section class="values">
  <p class="abs eyebrow">VARIOUS ASPECTS</p>
  <h2 class="abs slab values-title">Our Core Values</h2>
  <p class="abs values-text">Offering a strategic approach to project marketing and sales process, we offer:</p>
  <ul class="abs values-list">
    <li>Individually tailored marketing strategies</li>
    <li>End to end transaction management from deposit to handover</li>
  </ul>
  <div class="abs value" style="top:1318px">
    <div class="value-icon"><svg width="26" height="26" viewBox="0 0 26 26"><path d="M5 21 L7 15 L18 4 L22 8 L11 19 Z M5 21 L11 19" fill="none" stroke="#fff" stroke-width="2"/></svg></div>
    <h3 class="value-title">Our Core Values</h3>
    <p class="value-text">Our core values which are: Respect, pride, commitment, listen, innovation, form the foundation of how we conduct our day to day business and working relationships.</p>
  </div>
  <div class="abs divider"></div>
  <div class="abs value" style="top:1538px">
    <div class="value-icon"><svg width="26" height="26" viewBox="0 0 26 26"><path d="M13 3 A7 7 0 0 1 17 16 V19 H9 V16 A7 7 0 0 1 13 3 Z M10 22 H16" fill="none" stroke="#fff" stroke-width="2"/></svg></div>
    <h3 class="value-title" style="top:22px"># 1 Focus</h3>
    <p class="value-text" style="top:54px">Customer service is our #1 focus and our customer's satisfaction is how we measure our success.</p>
  </div>
</section>

<section>
  <div class="abs video-band" role="img" aria-label="Purple backdrop with scattered stationery and sweets"></div>
  <div class="abs video" role="img" aria-label="Explanation video still of a new two-storey home"></div>
  <svg class="abs play" width="70" height="70" viewBox="0 0 70 70"><circle cx="35" cy="35" r="32" fill="rgba(255,255,255,.2)" stroke="#fff" stroke-width="3"/><path d="M28 22 L50 35 L28 48 Z" fill="#fff"/></svg>
</section>

<section>
  <h2 class="abs slab cta-title">Ready To Get Started?</h2>
  <p class="abs cta-text">The 10-Minute conversation that will get you<br>on your way to your dream home</p>
  <a class="abs btn cta-btn">START HERE <svg width="18" height="10" viewBox="0 0 18 10"><path d="M0 5 H16 M12 1 L16 5 L12 9" fill="none" stroke="#fff" stroke-width="1.6"/></svg></a>
  <p class="abs cta-faq">or <a>Check FAQ</a></p>
</section>

<section class="abs builders">
  <span class="builder">Moritz</span>
  <span class="builder">G.T. Falwick</span>
  <span class="builder">PV Dwellings</span>
</section>

<section class="contact">
  <h2 class="abs contact-title">GET IN<br>TOUCH<br>WITH US</h2>
  <p class="abs contact-line" style="top:3651px"><svg width="14" height="14" viewBox="0 0 14 14"><path d="M3 1 L5 1 L6 4 L4.5 5.5 Q6 8.5 8.5 9.5 L10 8 L13 9 L13 11 Q13 13 11 13 Q1 12 1 3 Q1 1 3 1 Z" fill="#8c6bc4"/></svg>+1 555-010-4590</p>
  <p class="abs contact-line" style="top:3689px"><svg width="14" height="11" viewBox="0 0 14 11"><rect width="14" height="11" rx="1" fill="#8c6bc4"/><path d="M1 1 L7 6 L13 1" fill="none" stroke="#fff" stroke-width="1.2"/></svg>hello@freshnestguide.com</p>

  <div class="abs field" style="top:3337px"><label>NAME</label><span>Jane &amp; John Doe</span><svg width="16" height="12" viewBox="0 0 16 12"><path d="M1 6 L6 11 L15 1" fill="none" stroke="#8bc34a" stroke-width="2"/></svg></div>
  <div class="abs field" style="top:3396px"><label>COMPANY</label></div>
  <div class="abs field" style="top:3458px"><label>PHONE</label><i class="req-star">*</i></div>
  <div class="abs field" style="top:3518px"><label>MESSAGE</label></div>
  <div class="abs field" style="top:3562px"></div>
  <p class="abs required"><b>*</b>Required Field</p>
  <a class="abs btn submit">SUBMIT</a>
</section>

</body>
</html>
```